Scripture-Rooted Harvest Church of Cedar Hollow 2024 Theme

We, Scripture-Rooted Harvest Church of Cedar Hollow, need a design for two banners; (1) a Horizontal 6' x 4' banner that will be placed on one wall in the main sanctuary, (2) a retractable banner. The banners are to communicate/advertise the church's theme for 2024, "Endeavoring to Grow, Know and Love God More in 2024" (2 Timothy 2:15). The design should include our logo and church name. Use the color purple. This banner should be reflective of growth, knowledge, love of God. Our congregation demographic is 98% African American, 2% Hispanic. Our home base is Tampa, Florida (USA), but we have a small social media following.

Target Market(s)

Church members and visitors; male and female ages 1-99

Industry/Entity Type

Religious

Colors
6B429C
8869AF
B7A5CE
E3DAEB
F3F0F8

Requirements
Must have
• Church logo, color purple
Nice to have
• Vibrant design; colors that complement purple

```html
<!DOCTYPE html>
<html lang="en">
<head>
<meta charset="utf-8">
<title>Scripture-Rooted Harvest Church of Cedar Hollow – 2024 Theme Banners</title>
<link href="https://fonts.googleapis.com/css2?family=Oswald:wght@400;600&display=swap" rel="stylesheet">
<style>
  :root {
    --purple-deep: #3a1a6e;
    --purple: #6B429C;
    --purple-mid: #8869AF;
    --purple-soft: #B7A5CE;
    --lavender: #E3DAEB;
    --mist: #F3F0F8;
    --violet-glow: #b04fd6;
    --white: #ffffff;
  }
  * { box-sizing: border-box; margin: 0; padding: 0; }
  html, body { width: 802px; height: 1200px; overflow: hidden; background: var(--white); }
  body { position: relative; font-family: "Oswald", sans-serif; color: var(--white); }

  .banner { position: absolute; overflow: hidden; text-align: center; }
  .banner--retractable { left: 256px; top: 27px; width: 422px; height: 614px; }
  .banner--wall { left: 32px; top: 667px; width: 743px; height: 486px; }

  .banner__photo { position: absolute; inset: 0; }
  .banner--retractable .banner__photo {
    background:
      radial-gradient(ellipse at 55% 78%, rgba(227,218,235,.45) 0%, rgba(183,165,206,0) 45%),
      radial-gradient(ellipse at 30% 95%, rgba(176,79,214,.5) 0%, rgba(107,66,156,0) 50%),
      linear-gradient(180deg, #4b2a8a 0%, var(--purple) 45%, #7a4fb0 75%, #5c3594 100%);
  }
  .banner--wall .banner__photo {
    background:
      radial-gradient(ellipse at 65% 55%, rgba(20,8,40,.55) 0%, rgba(20,8,40,0) 35%),
      radial-gradient(ellipse at 85% 30%, rgba(227,218,235,.35) 0%, rgba(227,218,235,0) 40%),
      radial-gradient(ellipse at 15% 80%, rgba(176,79,214,.55) 0%, rgba(176,79,214,0) 45%),
      linear-gradient(120deg, #8a3fb8 0%, #9b4cc6 40%, #6a2f9e 70%, #8d45bf 100%);
  }

  .brand { position: absolute; display: flex; flex-direction: column; align-items: center; }
  .brand__mark { border-radius: 50%; background: var(--lavender); }
  .brand__name {
    font-weight: 600; color: var(--white); text-transform: uppercase;
    letter-spacing: .02em; line-height: 1.1; text-align: center;
  }
  .banner--retractable .brand { left: 0; right: 0; top: 48px; }
  .banner--retractable .brand__mark { width: 80px; height: 80px; }
  .banner--retractable .brand__name { margin-top: 12px; font-size: 15px; width: 240px; }
  .banner--wall .brand { left: 14px; top: 30px; width: 120px; }
  .banner--wall .brand__mark { width: 80px; height: 80px; }
  .banner--wall .brand__name { margin-top: 8px; font-size: 11px; }

  .theme { position: absolute; left: 0; right: 0; text-transform: uppercase; line-height: 1; }
  .theme__lead { display: block; font-weight: 600; }
  .theme__line { display: block; font-weight: 400; }
  .theme__year { display: block; font-weight: 600; }
  .banner--retractable .theme { top: 180px; }
  .banner--retractable .theme__lead { font-size: 36px; }
  .banner--retractable .theme__line { font-size: 25px; margin-top: 6px; }
  .banner--retractable .theme__year { font-size: 80px; margin-top: 4px; }
  .banner--wall .theme { top: 212px; }
  .banner--wall .theme__lead { font-size: 38px; }
  .banner--wall .theme__line { font-size: 27px; margin-top: 6px; }
  .banner--wall .theme__year { font-size: 86px; margin-top: 4px; }

  .invite { position: absolute; left: 0; right: 0; top: 530px; font-weight: 600; }
  .invite__label { display: block; font-size: 12px; letter-spacing: .06em; }
  .invite__url { display: block; font-size: 15px; margin-top: 10px; }
</style>
</head>
<body>

<section class="banner banner--retractable">
  <div class="banner__photo" role="img" aria-label="Purple-toned photo of raised hands in worship with an open Bible"></div>
  <div class="brand">
    <span class="brand__mark"></span>
    <span class="brand__name">Scripture-Rooted Harvest Church of Cedar Hollow</span>
  </div>
  <h1 class="theme">
    <span class="theme__lead">Endeavoring to Grow</span>
    <span class="theme__line">Know and Love God More in</span>
    <span class="theme__year">2024</span>
  </h1>
  <p class="invite">
    <span class="invite__label">JOIN US</span>
    <span class="invite__url">harvestcedarhollow.org</span>
  </p>
</section>

<section class="banner banner--wall">
  <div class="banner__photo" role="img" aria-label="Purple-toned photo of an open Bible with soft light flares"></div>
  <div class="brand">
    <span class="brand__mark"></span>
    <span class="brand__name">Scripture-Rooted Harvest Church of Cedar Hollow</span>
  </div>
  <h2 class="theme">
    <span class="theme__lead">Endeavoring to Grow</span>
    <span class="theme__line">Know and Love God More in</span>
    <span class="theme__year">2024</span>
  </h2>
</section>

</body>
</html>
```